Brenvick Holdings LLC, new Business cards

I'm moving offices and need new cards. Plus I'm open to modifying the current design of my card. I will keep the logo but would like to explore other layouts and fonts for the design. I've included the current double sided card for reference. I Like the navy color and white. Might be open to grays or silver. Needs to be clean and elegant.

Target Market(s)

Investors, buyers & sellers of private equities and real estate.

Contact Information for Business Card

Brenvick Holdings
Dorian P.K. Halvers, Managing Principal
418 Ostrander Ave., Suite 612
Denver, CO 80319
M: 970-555-0147, O: 303-555-0192
Dorian@brenvickholdings.example
Brenvickholdings.example

Colors
0354a2
ffffff
c4c4c4

Requirements
Must have
• Business card details.
• Logo raised or embossed, it was designed after a wax seal. Current has raised ink.
Nice to have
• Space on card to write additional notes.

```html
<!DOCTYPE html>
<html lang="en">
<head>
<meta charset="utf-8">
<title>Brenvick Holdings – Business Cards</title>
<link rel="stylesheet" href="https://fonts.googleapis.com/css2?family=Open+Sans:wght@400;600;700&family=Roboto+Slab:wght@400;700&family=Roboto:wght@400&display=swap">
<style>
  :root {
    --navy: #28226c;
    --navy-soft: #2f2978;
    --white: #ffffff;
    --ghost: #f1f0f3;
    --gray-text: #6b6b70;
    --stage: #e6e6e8;
  }
  * { box-sizing: border-box; margin: 0; padding: 0; }
  html, body { width: 1200px; height: 850px; overflow: hidden; }
  body {
    background: var(--stage);
    display: flex;
    align-items: center;
    justify-content: center;
    gap: 40px;
  }
  .card {
    position: relative;
    width: 540px;
    height: 309px;
    border-radius: 3px;
    overflow: hidden;
    box-shadow: 0 6px 18px rgba(0,0,0,0.18);
  }

  /* Front */
  .card-front { background: var(--navy); color: var(--white); }
  .front-decoration {
    position: absolute; inset: 0;
    background:
      radial-gradient(ellipse 120px 150px at 22% 40%, var(--navy-soft) 60%, transparent 62%),
      radial-gradient(ellipse 140px 170px at 82% 62%, var(--navy-soft) 60%, transparent 62%);
  }
  .front-mark {
    position: absolute; left: 0; right: 0; top: 58px;
    display: flex; flex-direction: column; align-items: center; gap: 14px;
  }
  .front-mark .seal-disc {
    width: 74px; height: 74px; border-radius: 50%;
    background: var(--white);
  }
  .front-mark .company-name {
    font-family: "Open Sans", sans-serif;
    font-weight: 700; font-size: 24px; letter-spacing: 1.5px;
  }
  .front-services {
    position: absolute; left: 26px; right: 26px; bottom: 24px;
    display: flex; justify-content: space-between;
    font-family: "Open Sans", sans-serif;
    font-weight: 600; font-size: 10.5px; letter-spacing: 1px;
    color: var(--white);
  }

  /* Back */
  .card-back { background: var(--white); }
  .back-decoration {
    position: absolute; inset: 0;
    background:
      radial-gradient(ellipse 110px 130px at 34% 32%, var(--ghost) 60%, transparent 62%),
      radial-gradient(ellipse 130px 170px at 74% 60%, var(--ghost) 60%, transparent 62%);
  }
  .holder {
    position: absolute; left: 0; top: 72px;
    padding-left: 30px;
  }
  .holder::before {
    content: ""; position: absolute; left: 0; top: 2px;
    width: 14px; height: 26px; background: var(--navy);
  }
  .holder-name {
    font-family: "Roboto Slab", serif; font-weight: 400;
    font-size: 20px; line-height: 24px; color: var(--navy); letter-spacing: 0.5px;
  }
  .holder-title {
    font-family: "Roboto Slab", serif; font-weight: 700;
    font-size: 9px; color: var(--navy); letter-spacing: 0.6px;
  }
  .contact-list {
    position: absolute; left: 22px; top: 126px;
    list-style: none;
    font-family: "Roboto", sans-serif; font-size: 12.5px; color: var(--gray-text);
  }
  .contact-list li { display: flex; align-items: center; gap: 9px; line-height: 19px; }
  .contact-list svg { width: 11px; height: 11px; fill: var(--navy); flex: none; }
  .back-mark {
    position: absolute; right: 22px; top: 22px;
    display: flex; align-items: center; gap: 7px;
    font-family: "Roboto Slab", serif; font-size: 10px; color: var(--navy);
  }
  .back-mark .seal-disc { width: 30px; height: 30px; border-radius: 50%; background: var(--navy); }
  .office-address {
    position: absolute; right: 26px; bottom: 22px;
    text-align: right; font-style: normal;
    font-family: "Roboto Slab", serif; font-size: 12.5px; line-height: 17px; color: var(--gray-text);
  }
  .office-address .office-name { color: var(--navy); font-size: 13.5px; margin-bottom: 6px; }
</style>
</head>
<body>

<section class="card card-front">
  <div class="front-decoration" role="img" aria-label="Faint heraldic lion silhouettes in tone on navy"></div>
  <div class="front-mark">
    <div class="seal-disc"></div>
    <div class="company-name">BRENVICK HOLDINGS</div>
  </div>
  <div class="front-services">
    <span>FAMILY OFFICE INVESTMENT FIRM</span><span>|</span>
    <span>PRIVATE EQUITY</span><span>|</span>
    <span>REAL ESTATE</span>
  </div>
</section>

<section class="card card-back">
  <div class="back-decoration" role="img" aria-label="Faint pale gray heraldic lion silhouettes"></div>
  <div class="back-mark"><span>Brenvick Holdings</span><div class="seal-disc"></div></div>

  <div class="holder">
    <div class="holder-name">DORIAN P.K. HALVERS</div>
    <div class="holder-title">MANAGING PRINCIPAL</div>
  </div>

  <ul class="contact-list">
    <li><svg viewBox="0 0 12 12"><rect x="3" y="0" width="6" height="12" rx="1.2"/><rect x="4" y="1.5" width="4" height="7.5" fill="#fff"/></svg>970-555-0147</li>
    <li><svg viewBox="0 0 12 12"><path d="M2.5 0.5 L4.5 0.5 L5.5 3.5 L4 4.6 Q5.2 7 7.4 8 L8.5 6.5 L11.5 7.5 L11.5 9.5 Q11 11.5 9 11.5 Q1 10.5 0.5 3 Q0.5 1 2.5 0.5Z"/></svg>303-555-0192</li>
    <li><svg viewBox="0 0 12 12"><rect x="0" y="2" width="12" height="8"/><path d="M0.5 2.5 L6 7 L11.5 2.5" stroke="#fff" stroke-width="1" fill="none"/></svg>Dorian@brenvickholdings.example</li>
    <li><svg viewBox="0 0 12 12"><circle cx="6" cy="6" r="6"/><path d="M0 6 H12 M6 0 V12 M2 2.5 Q6 4.5 10 2.5 M2 9.5 Q6 7.5 10 9.5" stroke="#fff" stroke-width="0.8" fill="none"/></svg>www.brenvickholdings.example</li>
  </ul>

  <address class="office-address">
    <div class="office-name">Brenvick Holdings LLC</div>
    418 Ostrander Ave.,<br>Suite 612<br>Denver, CO 80319
  </address>
</section>

</body>
</html>
```